We are a small business - Tree Care Company owned bt a certified Arborist. We would like an advertis

Hurricane season is approaching. We would like our current and potential customers to hire us for their tree work - safety first.

A little bit about us:

We are GWF-certified and insured, you can be confident that you will be able to trust us on your property. We maintain a clean, organized, and safe working environment.

Our tree service services St Petersburg, Clearwater, Belleair, Seminole, and surrounding tampa bay areas cover anything and everything that you may find yourself needing regarding tree care services.

Some of our specialties include tree pruning and trimming, removal, support, planting, emergency tree service, and much, much more.

For hurricane prep, make sure your trees are properly maintained and inspected for structual issues.

Target Market(s)

late 20's to 65. Homeow

Requirements
Must have
• A Call to action. Call us to schedule a FREE estimate.
• 1-866-413-BOUGH

```html
<!DOCTYPE html>
<html lang="en">
<head>
<meta charset="utf-8">
<title>Bayline Tree Co – Hurricane Season Flyer</title>
<link href="https://fonts.googleapis.com/css2?family=Lato:wght@400;700&family=Montserrat:wght@700;800&display=swap" rel="stylesheet">
<style>
  :root {
    --green: #17823a;
    --green-dark: #0f6a2c;
    --grass: #7cb02e;
    --yellow: #f7c51e;
    --ink: #1d1d1d;
    --page: #4a4a4a;
    --white: #ffffff;
  }
  html, body { margin: 0; padding: 0; width: 1200px; height: 1200px; overflow: hidden; background: var(--page); }
  .flyer {
    position: absolute; left: 180px; top: 12px; width: 840px; height: 1176px;
    background: var(--white); overflow: hidden;
    font-family: "Lato", Arial, sans-serif; color: var(--ink);
  }
  .hero-photo {
    position: absolute; left: 0; top: 0; width: 840px; height: 600px;
    background: linear-gradient(115deg, #0e120c 0%, #2b3a22 30%, #4f5a2a 48%, #b58f1c 62%, #e0ac22 78%, #3a3320 100%);
  }
  .shapes { position: absolute; left: 0; top: 0; width: 840px; height: 1176px; }
  .brand { position: absolute; left: 62px; top: 78px; color: var(--white); text-align: center; width: 320px; }
  .brand-name { font-size: 44px; font-weight: 400; letter-spacing: 0.5px; line-height: 1; }
  .brand-tag { margin-top: 12px; padding-top: 8px; border-top: 1px solid var(--white); font-size: 14px; letter-spacing: 4px; }
  .cta {
    position: absolute; left: 515px; top: 420px; width: 314px; height: 298px;
    color: var(--white); text-align: center;
  }
  .cta-lead { margin-top: 28px; font-size: 40px; font-weight: 700; line-height: 1.1; }
  .cta-sub { margin-top: 8px; font-size: 29px; line-height: 1.25; }
  .cta-phone { margin-top: 14px; font-family: "Montserrat", Arial, sans-serif; font-weight: 800; color: var(--yellow); font-size: 40px; line-height: 1.15; }
  .cta-phone span { display: block; font-size: 33px; }
  .section-title { position: absolute; left: 49px; margin: 0; font-family: "Montserrat", Arial, sans-serif; font-weight: 800; color: var(--green); font-size: 21px; letter-spacing: 0.5px; }
  .about-title { top: 634px; }
  .about-body { position: absolute; left: 49px; top: 667px; width: 420px; margin: 0; font-size: 14.4px; line-height: 18.3px; }
  .specialties-title { top: 815px; }
  .specialties { position: absolute; left: 48px; top: 858px; margin: 0; padding: 0; list-style: none; font-size: 20px; }
  .specialties li { position: relative; padding-left: 46px; height: 33px; line-height: 26px; }
  .specialties li.multi { height: auto; line-height: 26px; }
  .specialties svg { position: absolute; left: 0; top: 1px; width: 26px; height: 26px; }
  .photo-circle { position: absolute; border-radius: 50%; }
  .photo-crew { left: 342px; top: 918px; width: 244px; height: 244px;
    background: radial-gradient(circle at 50% 30%, #6fa7d8 0%, #5a8a4a 55%, #8fd14b 100%); }
  .photo-truck { left: 520px; top: 806px; width: 348px; height: 348px;
    background: linear-gradient(180deg, #3f6b2c 0%, #7a9a5a 40%, #e9ecee 60%, #8a8a86 100%); }
  .badge { position: absolute; left: 42px; top: 1066px; width: 58px; height: 104px; background: var(--green); border: 3px solid #f2e8a0; box-sizing: border-box; }
</style>
</head>
<body>
<main class="flyer">
  <div class="hero-photo" role="img" aria-label="Tree crew in hi-vis shirts working beside a yellow stump grinder"></div>

  <svg class="shapes" viewBox="0 0 840 1176" aria-hidden="true">
    <path d="M0,430 C130,510 280,540 420,490 C560,440 700,380 840,370 L840,1176 L0,1176 Z" fill="var(--green)"/>
    <path d="M0,446 C130,526 280,556 420,506 C560,456 700,396 840,386 L840,1176 L0,1176 Z" fill="var(--white)"/>
    <path d="M0,452 C130,532 280,562 420,512 C560,462 700,402 840,392 L840,1176 L0,1176 Z" fill="var(--green-dark)"/>
    <path d="M0,474 C130,556 280,580 420,530 C560,480 700,424 840,414 L840,1176 L0,1176 Z" fill="var(--white)"/>
    <rect x="515" y="405" width="314" height="313" rx="6" fill="var(--green)"/>
    <path d="M0,1086 C30,1070 70,1066 110,1080 C150,1090 170,1074 210,1092 C250,1106 280,1120 320,1118 L400,1140 C440,1150 470,1132 520,1130 L840,1110 L840,1176 L0,1176 Z" fill="var(--grass)"/>
    <circle cx="464" cy="1040" r="131" fill="none" stroke="var(--green)" stroke-width="3"/>
    <circle cx="694" cy="980" r="190" fill="none" stroke="var(--green)" stroke-width="3"/>
  </svg>

  <div class="brand">
    <div class="brand-name">Bayline Tree Co</div>
    <div class="brand-tag">PROFESSIONAL TREE CARE</div>
  </div>

  <div class="cta">
    <div class="cta-lead">Call us to</div>
    <div class="cta-sub">schedule a FREE<br>estimate</div>
    <div class="cta-phone">1-866-413<span>-BOUGH</span></div>
  </div>

  <h2 class="section-title about-title">ABOUT US</h2>
  <p class="about-body">We are GWF-certified and insured, you can be confident that you will be able to trust us on your property. We maintain a clean, organized, and safe working environment.<br>Our tree service services St Petersburg, Clearwater, Belleair, Seminole, and surrounding tampa bay areas cover anything and everything that you may find yourself needing regarding tree care services</p>

  <h2 class="section-title specialties-title">OUR SPECIALTIES</h2>
  <ul class="specialties">
    <li><svg viewBox="0 0 26 26"><circle cx="13" cy="13" r="11.5" fill="none" stroke="var(--green)" stroke-width="1.6"/><path d="M8,7 L18,19 M18,7 L8,19" stroke="var(--ink)" stroke-width="2"/></svg>Tree pruning and Trimming</li>
    <li><svg viewBox="0 0 26 26"><circle cx="13" cy="13" r="11.5" fill="none" stroke="var(--green)" stroke-width="1.6"/><rect x="7" y="11" width="12" height="7" fill="var(--ink)"/></svg>Removal</li>
    <li><svg viewBox="0 0 26 26"><circle cx="13" cy="13" r="11.5" fill="none" stroke="var(--green)" stroke-width="1.6"/><circle cx="13" cy="12" r="4" fill="var(--ink)"/><path d="M7,18 H19" stroke="var(--ink)" stroke-width="2"/></svg>Support</li>
    <li><svg viewBox="0 0 26 26"><circle cx="13" cy="13" r="11.5" fill="none" stroke="var(--green)" stroke-width="1.6"/><path d="M13,18 V10 M13,12 C10,9 9,8 9,7 M13,11 C16,8 17,8 17,7" stroke="var(--ink)" stroke-width="2" fill="none"/></svg>Planting</li>
    <li class="multi"><svg viewBox="0 0 26 26"><circle cx="13" cy="13" r="11.5" fill="none" stroke="var(--green)" stroke-width="1.6"/><path d="M14,6 L9,14 H13 L11,20 L17,11 H13 Z" fill="var(--ink)"/></svg>Emergency tree service<br>and much, much more</li>
  </ul>

  <div class="badge" role="img" aria-label="Certification badge"></div>
  <div class="photo-circle photo-truck" role="img" aria-label="White bucket truck on a residential street with crew at work"></div>
  <div class="photo-circle photo-crew" role="img" aria-label="Arborist in a hard hat looking up at tall pine trees"></div>
</main>
</body>
</html>
```